Create Social Media design templates for Online-Education-Startup

We are an online platform for pupils who provide group courses and on demand individual tutroing lessons. Our core values are personalisation, family and success. We need a holistic social media design concept which includes nine possible layouts for Instagram posts which reflect our values and promote not only our offerings and special deals but also support in building our brand image (for example: telling company history, daily news, funny facts, getting to know the team etc.).
Additionally, we need design elements for our Vidstream channel:
-Videocover
-Cover Image for the channel

Our main colour is orange (RGB-Code: 255;105;31) and additional colours white, black, and grey. For the reference have a look at our website: www.lernquorvo.de.

Target Market(s)

We want to attract customers to our online tutoring courses and build a brand.

Industry/Entity Type

Education / Tutoring

Font styles to use
Sans Serif

Requirements
Must have
• Familiarize yourself with the style of our website. The designs should fit as well as possible.

```html
<!DOCTYPE html>
<html lang="en">
<head>
<meta charset="utf-8">
<title>Lernquorvo – Video Channel Design</title>
<link rel="stylesheet" href="https://fonts.googleapis.com/css2?family=Open+Sans:wght@400;600;700;800&family=Roboto:wght@400;500;700&display=swap">
<style>
:root{
  --orange:#ff691f;
  --orange-soft:#ffc4a4;
  --white:#ffffff;
  --black:#111111;
  --ink:#222222;
  --grey-page:#999999;
  --grey-band:#f4f4f4;
  --grey-banner:#d6d6d6;
  --grey-text:#777777;
  --line:#dddddd;
  --red:#e52d27;
  --tile:#2b2b2e;
  --violet:#7c5cff;
}
*{box-sizing:border-box;margin:0;padding:0}
html,body{width:927px;height:1200px;overflow:hidden}
body{position:relative;background:var(--grey-page);font-family:"Open Sans",sans-serif;color:var(--ink)}
.channel-page{position:absolute;left:0;top:0;width:927px;height:609px;background:var(--white)}
.topbar{position:absolute;left:0;top:0;width:927px;height:29px;border-bottom:1px solid var(--line);border-top:1px solid var(--line)}
.topbar .menu{position:absolute;left:147px;top:11px;width:10px;height:7px;border-top:1px solid #999;border-bottom:1px solid #999}
.topbar .menu::after{content:"";position:absolute;left:0;top:2px;width:10px;border-top:1px solid #999}
.topbar .site-name{position:absolute;left:170px;top:8px;font:700 9px "Roboto",sans-serif;color:var(--red)}
.topbar .search{position:absolute;left:257px;top:7px;width:285px;height:15px;border:1px solid var(--line)}
.topbar .search::after{content:"";position:absolute;right:0;top:0;width:32px;height:13px;background:#f3f3f3;border-left:1px solid var(--line)}
.topbar .icon{position:absolute;top:10px;width:7px;height:8px;background:#aaa;border-radius:2px}
.topbar .avatar{position:absolute;left:784px;top:7px;width:16px;height:16px;border-radius:50%;background:#333}
.banner{position:absolute;left:185px;top:29px;width:578px;height:158px;background:var(--grey-banner);overflow:hidden}
.banner svg{position:absolute;left:0;top:0}
.brand{position:absolute;display:flex;align-items:center;gap:6px}
.brand .dot{border-radius:50%;background:var(--orange);flex:none}
.brand .name{color:var(--ink);font-weight:700;line-height:1.15}
.banner .brand{left:62px;top:25px}
.banner .brand .dot{width:30px;height:30px}
.banner .brand .name{font-size:13px}
.tagline{position:absolute;left:74px;top:91px;width:421px;height:27px;background:rgba(240,240,240,.92);font-size:13.5px;line-height:27px;padding-left:12px;color:#333;white-space:nowrap}
.tagline em{font-style:normal;font-weight:600;color:var(--orange)}
.channel-head{position:absolute;left:0;top:187px;width:927px;height:74px;background:var(--grey-band)}
.channel-head .logo-tile{position:absolute;left:147px;top:8px;width:40px;height:40px;border-radius:50%;background:var(--white);display:flex;align-items:center;justify-content:center}
.channel-head .logo-tile span{width:12px;height:12px;border-radius:50%;background:var(--orange)}
.channel-title{position:absolute;left:199px;top:16px;font:600 11px "Open Sans",sans-serif}
.channel-subs{position:absolute;left:199px;top:32px;font:400 6.5px "Roboto",sans-serif;color:var(--grey-text)}
.subscribe{position:absolute;left:708px;top:18px;width:93px;height:21px;background:var(--red);color:var(--white);font:500 7px/21px "Roboto",sans-serif;text-align:center;letter-spacing:.3px}
.tabs{position:absolute;left:0;top:56px;width:927px;font:500 6.5px "Roboto",sans-serif;color:#888;letter-spacing:.3px}
.tabs span{position:absolute;top:0}
.tabs .active{color:var(--ink)}
.tabs .underline{position:absolute;left:147px;top:15px;width:52px;height:2px;background:#555}
.tabs .search-tab{width:8px;height:8px;border:1px solid #888;border-radius:50%}
.featured-thumb{position:absolute;left:147px;top:272px;width:306px;height:175px}
.featured-info{position:absolute;left:474px;top:275px;width:260px}
.featured-info h2{font:700 8px "Open Sans",sans-serif}
.featured-info .meta{font:400 5px "Roboto",sans-serif;color:var(--grey-text);margin-top:4px}
.featured-info p{font:400 5.6px/10.5px "Roboto",sans-serif;color:#666;margin-top:8px}
.featured-info hr{border:0;border-top:1px dashed #bbb;margin:12px 0 8px}
.divider{position:absolute;left:147px;top:459px;width:655px;border-top:1px solid var(--line)}
.uploads-head{position:absolute;left:147px;top:472px;font:600 7px "Roboto",sans-serif}
.uploads-head .play{margin-left:14px;font-weight:400;color:#999}
.uploads{position:absolute;left:147px;top:494px;display:flex;gap:1px}
.video{width:108px}
.video .thumb{position:relative;height:61px;background:var(--tile)}
.video .thumb .badge{position:absolute;right:5px;top:5px;width:7px;height:7px;border:1px solid var(--violet);border-radius:50%}
.video .thumb .hl{position:absolute;left:5px;top:39px;font:italic 800 8px "Open Sans",sans-serif;color:var(--white);letter-spacing:-.3px}
.video .thumb .sub{position:absolute;left:6px;top:50px;font:600 3px "Roboto",sans-serif;color:var(--violet)}
.video .title{font:700 5.8px "Open Sans",sans-serif;margin-top:5px}
.video .meta{font:400 4.5px "Roboto",sans-serif;color:#999;margin-top:2px}
.video-cover{position:absolute;left:51px;top:676px;width:825px;height:463px}
</style>
</head>
<body>

<section class="channel-page">
  <header class="topbar">
    <span class="menu"></span>
    <span class="site-name">Vidstream</span>
    <span class="search"></span>
    <span class="icon" style="left:735px"></span>
    <span class="icon" style="left:760px"></span>
    <span class="avatar"></span>
  </header>

  <div class="banner">
    <svg width="578" height="158" viewBox="0 0 578 158">
      <defs>
        <linearGradient id="bannerPhoto" x1="0" y1="0" x2="1" y2="1">
          <stop offset="0" stop-color="#e9e6e3"/>
          <stop offset=".5" stop-color="#c9d2e2"/>
          <stop offset="1" stop-color="#b7a79a"/>
        </linearGradient>
      </defs>
      <polygon points="286,0 578,0 578,158 340,158" fill="url(#bannerPhoto)" role="img" aria-label="Photo: two students working together at a desk"/>
      <line x1="286" y1="0" x2="340" y2="158" stroke="#111" stroke-width="2.5"/>
      <rect x="0" y="144" width="578" height="2" fill="var(--orange)"/>
      <rect x="0" y="149" width="578" height="1.5" fill="var(--orange)"/>
    </svg>
    <div class="brand"><span class="dot"></span><span class="name">Lernquorvo<br><span style="font-weight:400">Bildungsinstitut</span></span></div>
    <div class="tagline">Our core values are <em>personalisation</em>, <em>family</em> and <em>success</em>.</div>
  </div>

  <div class="channel-head">
    <div class="logo-tile"><span></span></div>
    <div class="channel-title">Lernquorvo Bildungsinstitut</div>
    <div class="channel-subs">500.000 subscribers</div>
    <div class="subscribe">SUBSCRIBE</div>
    <nav class="tabs">
      <span class="active" style="left:162px">HOME</span>
      <span style="left:216px">VIDEOS</span>
      <span style="left:274px">PLAYLISTS</span>
      <span style="left:336px">CHANNELS</span>
      <span style="left:399px">DISCUSSION</span>
      <span style="left:471px">ABOUT</span>
      <span class="search-tab" style="left:528px"></span>
      <i class="underline"></i>
    </nav>
  </div>

  <svg class="featured-thumb" viewBox="0 0 825 463" preserveAspectRatio="none">
    <rect width="825" height="463" fill="var(--orange)"/>
    <polygon points="236,0 710,0 470,463 0,463" fill="#8e5b4e" role="img" aria-label="Photo: pupil writing at a desk with two tutors beside him"/>
    <polygon points="228,0 236,0 0,463 0,448" fill="var(--white)"/>
    <polygon points="710,0 730,0 490,463 470,463" fill="var(--white)"/>
    <circle cx="55" cy="60" r="17" fill="var(--white)"/>
    <text x="82" y="55" font-family="Open Sans, sans-serif" font-weight="700" font-size="14" fill="var(--white)">Lernquorvo</text>
    <text x="82" y="71" font-family="Open Sans, sans-serif" font-weight="700" font-size="14" fill="var(--white)">Bildungsinstitut</text>
    <rect x="0" y="319" width="825" height="80" fill="var(--orange-soft)" opacity=".9"/>
    <text x="412" y="351" text-anchor="middle" font-family="Open Sans, sans-serif" font-size="23" fill="var(--black)">We are an online platform for pupils</text>
    <text x="412" y="381" text-anchor="middle" font-family="Open Sans, sans-serif" font-weight="700" font-size="22" fill="var(--black)">who provide group courses and on demand individual tutroing lessons.</text>
  </svg>

  <div class="featured-info">
    <h2>Editable Video Name - Exemple</h2>
    <div class="meta">500.000 views · 1 day ago</div>
    <p>Join our tutors for a clear walkthrough of fractions, with worked examples, practice tasks and tips for the next class test. Every step is explained slowly so pupils can follow along at home and pause whenever they need a moment to think it through again.</p>
    <hr>
    <p style="margin-top:0">Book a personal lesson or join a small group course on our platform and learn together with pupils from all over the country.</p>
  </div>

  <div class="divider"></div>
  <div class="uploads-head">UPLOADS<span class="play">PLAY ALL</span></div>

  <div class="uploads">
    <article class="video"><div class="thumb"><i class="badge"></i><span class="hl">THUMBNAIL HIGHLIGHT</span><span class="sub">NEW LESSON EVERY WEEK</span></div><div class="title">Editable Video Name - Exemple</div><div class="meta">100.000 views · 2 days ago</div></article>
    <article class="video"><div class="thumb"><i class="badge"></i><span class="hl">THUMBNAIL HIGHLIGHT</span><span class="sub">NEW LESSON EVERY WEEK</span></div><div class="title">Editable Video Name - Exemple</div><div class="meta">200.000 views · 3 days ago</div></article>
    <article class="video"><div class="thumb"><i class="badge"></i><span class="hl">THUMBNAIL HIGHLIGHT</span><span class="sub">NEW LESSON EVERY WEEK</span></div><div class="title">Editable Video Name - Exemple</div><div class="meta">100.000 views · 4 days ago</div></article>
    <article class="video"><div class="thumb"><i class="badge"></i><span class="hl">THUMBNAIL HIGHLIGHT</span><span class="sub">NEW LESSON EVERY WEEK</span></div><div class="title">Editable Video Name - Exemple</div><div class="meta">200.000 views · 5 days ago</div></article>
    <article class="video"><div class="thumb"><i class="badge"></i><span class="hl">THUMBNAIL HIGHLIGHT</span><span class="sub">NEW LESSON EVERY WEEK</span></div><div class="title">Editable Video Name - Exemple</div><div class="meta">100.000 views · 6 days ago</div></article>
    <article class="video"><div class="thumb"><i class="badge"></i><span class="hl">THUMBNAIL HIGHLIGHT</span><span class="sub">NEW LESSON EVERY WEEK</span></div><div class="title">Editable Video Name - Exemple</div><div class="meta">100.000 views · 7 days ago</div></article>
  </div>
</section>

<svg class="video-cover" viewBox="0 0 825 463">
  <defs>
    <linearGradient id="coverPhoto" x1="0" y1="0" x2="1" y2="1">
      <stop offset="0" stop-color="#d8d2cc"/>
      <stop offset=".45" stop-color="#b3675a"/>
      <stop offset="1" stop-color="#7a2f35"/>
    </linearGradient>
  </defs>
  <rect width="825" height="463" fill="var(--orange)"/>
  <polygon points="236,0 710,0 470,463 0,463" fill="url(#coverPhoto)" role="img" aria-label="Photo: pupil writing at a desk with two tutors looking over his work"/>
  <polygon points="226,0 236,0 0,463 0,443" fill="var(--white)"/>
  <polygon points="710,0 726,0 486,463 470,463" fill="var(--white)"/>
  <circle cx="58" cy="60" r="20" fill="var(--white)"/>
  <text x="89" y="55" font-family="Open Sans, sans-serif" font-weight="700" font-size="13.5" fill="var(--black)">Lernquorvo</text>
  <text x="89" y="72" font-family="Open Sans, sans-serif" font-weight="700" font-size="13.5" fill="var(--black)">Bildungsinstitut</text>
  <rect x="0" y="319" width="825" height="80" fill="var(--orange-soft)" opacity=".88"/>
  <text x="412" y="352" text-anchor="middle" font-family="Open Sans, sans-serif" font-size="23" fill="var(--black)">We are an online platform for pupils</text>
  <text x="412" y="381" text-anchor="middle" font-family="Open Sans, sans-serif" font-weight="700" font-size="22" fill="var(--black)">who provide group courses and on demand individual tutroing lessons.</text>
</svg>

</body>
</html>
```